Flyer Design for Promoting Arborist Business

Hi guys,
***UPDATE: File pack is available here: https://www.filecrate-example.net/sh/x7k2qq/BBbR4tLmZ9wPdVs?dl=0
We've are a high-end arborist business in Edinburgh and we're now looking to create some promotional flyers to attract new business.
This is an open brief and we're looking for inspiration from our designer.
Our target market for the flyers is people who cannot readily access our online material (e.g. elderly people without internet access), so therefore has to be easily understood.
Trust is a central part of our business and we'd like our photographs on the flyer to build that trust.
The primary method of contact will be telephone, therefore we'd like our phone numbers to be front and centre.
You can see our website here: www.fernhollowtreecare.com
We have a full pack of design material for our logo which can be shared. This includes colours, fonts and logo. It's all as per our website.
Inspire us!
Best,
Malcolm

Look and feel
Each slider illustrates characteristics of the customer's brand and the style your logo design should communicate.

```html
<!DOCTYPE html>
<html lang="en">
<head>
<meta charset="utf-8">
<title>Fernhollow Tree Care – Flyer</title>
<link href="https://fonts.googleapis.com/css2?family=Open+Sans:wght@400;600&family=Archivo+Black&family=Tinos&display=swap" rel="stylesheet">
<style>
  :root{
    --red:#b01820;
    --red-dark:#7d0f14;
    --ink:#2a2a2a;
    --grey-text:#6b6b6b;
    --panel:#3a3a3d;
    --panel-dark:#2b2b2e;
    --white:#ffffff;
    --black:#141414;
  }
  *{box-sizing:border-box;margin:0;padding:0}
  html,body{width:915px;height:1200px;overflow:hidden;background:#fff}
  .flyer{position:relative;width:915px;height:1200px;background:var(--white);font-family:"Open Sans",sans-serif;overflow:hidden}

  .hero-photo{position:absolute;left:0;top:100px;width:915px;height:366px;
    background:linear-gradient(90deg,#1a1514 0%,#2e2622 35%,#6b5a4a 60%,#8d7a66 80%,#5d4e40 100%)}
  .header-shape{position:absolute;left:0;top:0;width:915px;height:215px}
  .emergency-tab{position:absolute;right:0;top:0;width:470px;height:80px;display:flex;align-items:center;justify-content:flex-end;padding-right:22px;
    font-family:"Tinos",serif;color:var(--white);font-size:26px;letter-spacing:.5px}
  .brand{position:absolute;left:30px;top:70px;display:flex;align-items:center;gap:14px}
  .brand-mark{width:34px;height:34px;border-radius:50%;background:var(--red)}
  .brand-name{font-family:"Tinos",serif;font-size:40px;line-height:1.05;color:var(--ink);letter-spacing:1px}
  .headline{position:absolute;left:30px;top:280px;font-family:"Archivo Black",sans-serif;color:var(--white);font-size:30px;line-height:38px;letter-spacing:1px;text-transform:uppercase}

  .intro{position:absolute;left:30px;top:503px;width:850px}
  .intro-lead{color:var(--red);font-size:21px;font-weight:600;letter-spacing:-.5px}
  .intro-sub{color:var(--red);font-size:20px;margin-top:4px}
  .intro-body{color:var(--grey-text);font-size:20.5px;line-height:27px;margin-top:18px;text-align:justify;letter-spacing:-.3px}
  .badges{position:absolute;left:698px;top:497px;display:flex;gap:18px}
  .badge-box{width:86px;height:62px;border:2px solid var(--red);border-radius:8px;background:linear-gradient(#fff 72%,var(--red) 72%)}
  .badge-plain{width:48px;height:58px;border-radius:4px;background:#e9e9e9}

  .services{position:absolute;left:0;top:724px;width:915px;height:248px}
  .services-rule{position:absolute;left:0;top:24px;width:915px;height:5px;background:var(--red)}
  .services-panel{position:absolute;left:0;top:27px;width:915px;height:220px;background:linear-gradient(90deg,var(--panel) 0%,#48484b 50%,var(--panel-dark) 100%);border-bottom:4px solid var(--red);display:flex;padding:40px 0 0 28px}
  .services-tab{position:absolute;left:0;top:0;width:457px;height:48px;background:var(--red);border-radius:0 24px 24px 0;color:var(--white);font-size:23px;font-weight:600;line-height:48px;padding-left:30px;z-index:1}
  .services-list{list-style:none}
  .services-list li{color:var(--white);font-size:20px;line-height:32px;height:32px;display:flex;align-items:center;gap:16px;white-space:nowrap}
  .services-list li::before{content:"›";width:17px;height:17px;border:1.5px solid var(--red);border-radius:50%;color:var(--red);font-size:14px;line-height:12px;text-align:center;flex:none}
  .col-1{width:310px}.col-2{width:290px}

  .planning{position:absolute;left:0;top:994px;width:915px;text-align:center;color:var(--grey-text);font-size:19px;line-height:31px;letter-spacing:-.4px}

  .footer-band{position:absolute;left:0;top:1061px;width:915px;height:139px}
  .phone-pill{position:absolute;left:223px;top:1090px;width:450px;height:54px;border-radius:27px;background:linear-gradient(var(--red),var(--red-dark));display:flex;align-items:center;justify-content:center;gap:14px;color:var(--white);font-size:40px;font-weight:600;letter-spacing:2px;box-shadow:0 4px 8px rgba(0,0,0,.5)}
  .website{position:absolute;left:0;top:1156px;width:915px;text-align:center;color:var(--white);font-size:23px;line-height:32px;letter-spacing:1.5px}
</style>
</head>
<body>
<main class="flyer">
  <div class="hero-photo" role="img" aria-label="Arborist in helmet and harness cutting a large tree trunk with a chainsaw above a rooftop"></div>

  <svg class="header-shape" viewBox="0 0 915 215" preserveAspectRatio="none" aria-hidden="true">
    <path d="M0 0H915V100H520C470 100 440 140 410 170C385 196 360 205 320 205H0Z" fill="#fff"/>
    <path d="M445 0H915V80H520C495 80 480 70 465 30Z" fill="#b01820"/>
  </svg>

  <div class="emergency-tab">24/7 EMERGENCY SERVICE</div>

  <div class="brand">
    <span class="brand-mark"></span>
    <span class="brand-name">FERNHOLLOW<br>TREE CARE</span>
  </div>

  <h1 class="headline">Professional<br>Edinburgh-based<br>tree surgeons</h1>

  <section class="intro">
    <p class="intro-lead">Looking for a professional tree surgeon in Edinburgh?</p>
    <p class="intro-sub">Give us a try!</p>
    <p class="intro-body">We're friendly, professional and dependable with a discerning eye for detail and a passion for tree care. Whether you need one or more trees reduced, trimmed or removed, we offer bespoke tree services to residential customers as well as commercial enterprises and government organisations.</p>
  </section>

  <div class="badges" aria-hidden="true">
    <div class="badge-box"></div>
    <div class="badge-plain"></div>
  </div>

  <section class="services">
    <div class="services-rule"></div>
    <div class="services-panel">
      <ul class="services-list col-1">
        <li>Aerial Pruning</li><li>Aerial Dismantling</li><li>Clear Felling</li><li>Crown Lifts</li><li>Crown Reductions</li>
      </ul>
      <ul class="services-list col-2">
        <li>Emergency Response</li><li>Garden Clearance</li><li>Sectional Felling</li><li>Site Clearance</li><li>Storm Damage</li>
      </ul>
      <ul class="services-list">
        <li>Stump Removal</li><li>Tree Surveys</li><li>Waste Removal</li><li>Wood Chipping</li><li>and much more</li>
      </ul>
    </div>
    <h2 class="services-tab">OUR SERVICES</h2>
  </section>

  <p class="planning">We offer a free planning application service to manage the necessary permissions<br>for trees with Tree Protection Orders (TPOs) and in Conservation Areas.</p>

  <svg class="footer-band" viewBox="0 0 915 139" preserveAspectRatio="none" aria-hidden="true">
    <defs>
      <linearGradient id="bandDark" x1="0" y1="0" x2="0" y2="1">
        <stop offset="0" stop-color="#2a2a2a"/><stop offset="1" stop-color="#0e0e0e"/>
      </linearGradient>
    </defs>
    <path d="M0 0C150 10 300 40 457 48C614 40 765 10 915 0V139H0Z" fill="#b01820"/>
    <path d="M0 20C150 30 300 55 457 62C614 55 765 30 915 20V139H0Z" fill="url(#bandDark)"/>
  </svg>

  <div class="phone-pill">
    <svg width="38" height="38" viewBox="0 0 38 38" aria-hidden="true">
      <circle cx="19" cy="19" r="16.5" fill="none" stroke="#fff" stroke-width="2.5"/>
      <path d="M13 10c1-1 2-1 3 0l2 3c.6 1 .4 1.8-.4 2.5l-1 .9c.8 2 2.6 3.8 4.6 4.6l.9-1c.7-.8 1.5-1 2.5-.4l3 2c1 1 1 2 0 3l-1.5 1.5c-5 1.5-15-8.5-13.5-13.5Z" fill="#fff"/>
    </svg>
    <span>0131 496 0725</span>
  </div>
  <p class="website">www.fernhollowtreecare.com</p>
</main>
</body>
</html>
```